Web Design Project for accounting firm

Hi winners
we are a chartered accountancy firm. We do really want to get into SEO. The link below is to our current website which I don't really like as it looks too simple.
www.plovetaxworks.com.au
In the homepage
I want to have Service tab, Testimonial tab, Events tab, Partner tab, blog tab and contact us tab
I want to have a section which have a bit description of the rencent blog and by clicking the section,you get into the real blogging page
I want a section which shows the most current client testimonials and by click into it, it gives you the testimonial page
I want a section for service which have a discription of the service overall and once click into more details, service details page pop up
I want a section for parter which had a bit description of the partner and linked to the detailed partner page
a section shows the contact number
a section for social media
a section for my logos, a section for GL logo and a section says "Liability limited by a scheme approved under Professional Standards Legislation"
In the first round, everyone can just design the homepage for me. And I will pick a couple for the second round to design the service page. and then I pick one to finish off the whole web design project.
below are the website I am planning to get
http://www.quenmarsh.com.au/
http://www.solvanbrookledger.com.au/ (my favourate)
Here is the link to download the GL logo
http://www.guildofledgerkeepers.com.au/Members/Marketing-your-practice/Logos
Hi Guys
I have reloaded the attachments. Hopefully works this time
I also add the link to the GL logo since someone has just asked
Will guarantee the payment when something good comes up. Won't wait until the due date.
Hi designers
I have guaranteed the payment. I am open to any good design now.
Marta
Accounting

```html
<!DOCTYPE html>
<html lang="en">
<head>
<meta charset="utf-8">
<title>Plove Tax Works — Chartered Accountants</title>
<link href="https://fonts.googleapis.com/css2?family=Archivo+Black&family=Cinzel:wght@400&family=Cormorant+Garamond:wght@500&family=Arimo:wght@400;700&display=swap" rel="stylesheet">
<style>
  :root{
    --black:#000;
    --white:#fff;
    --green:#12b822;
    --card-dark:rgba(58,58,58,.45);
    --card-deep:rgba(0,0,0,.55);
    --footer-bg:rgba(0,20,8,.88);
    --link-blue:#2f8fd6;
    --divider:#3a3a3a;
    --btn-top:#f2f2f2;
    --btn-bottom:#b9b9b9;
    --orange:#ef7a22;
    --sky:#7aaed6;
    --gold:#fcbc14;
  }
  *{box-sizing:border-box;margin:0;padding:0}
  html,body{width:1200px;height:1136px;overflow:hidden}
  body{
    position:relative;
    font-family:"Arimo",Arial,sans-serif;
    color:var(--white);
    background:linear-gradient(to bottom,var(--black) 0,var(--black) 640px,#0a5a14 720px,#0f9a1f 800px,var(--green) 860px,var(--green) 100%);
  }
  .site-header{position:absolute;left:0;top:0;width:1200px;height:141px;background:var(--black);border-bottom:1px solid var(--divider)}
  .brand{position:absolute;left:159px;top:7px;display:flex;align-items:flex-start;gap:18px}
  .brand-mark{width:93px;height:93px;border:2px solid var(--white)}
  .brand-name{font-family:"Cinzel",serif;font-size:46px;line-height:1;letter-spacing:.5px;margin-top:8px}
  .brand-tagline{font-family:"Cormorant Garamond",serif;font-size:19px;margin:12px 0 0 26px;letter-spacing:.3px}
  .account{position:absolute;right:159px;top:20px;display:flex;align-items:center;gap:10px;font-size:11px;letter-spacing:.4px}
  .phone{position:absolute;right:159px;top:56px;font-weight:700;font-size:27px}
  .main-nav{position:absolute;left:160px;top:114px;font-weight:700;font-size:13px}
  .main-nav a{position:absolute;color:var(--white);text-decoration:none;white-space:nowrap}
  .search{position:absolute;left:872px;top:112px;width:169px;height:20px;background:var(--white);border-radius:6px;color:#666;font-size:10px;padding:4px 9px}
  .search svg{position:absolute;right:6px;top:3px}
  .hero-title{position:absolute;left:161px;top:200px;font-family:"Archivo Black",sans-serif;font-size:75px;line-height:88px;letter-spacing:.5px}
  .hero-art{position:absolute;left:548px;top:183px;width:493px;height:211px;border-radius:14px;
    background:linear-gradient(90deg,#f08a3a 0%,#e8742a 28%,#8cb6d8 45%,#79a9d0 60%,#fcc63a 78%,#f8b418 100%)}
  .card{position:absolute;border-radius:6px}
  .card-tall{top:429px;width:263px;height:300px;background:linear-gradient(to bottom,#1c1c1c 0,#1c1c1c 70%,var(--card-dark) 90%)}
  .card-wide{top:757px;width:417px;height:169px;background:var(--card-deep)}
  .card h2{font-weight:400;font-size:29px;position:absolute;left:37px;top:26px;white-space:nowrap}
  .card p{position:absolute;left:37px;font-size:14px;line-height:28px}
  .card-tall p{top:80px;width:200px}
  .card-wide p{top:83px;width:225px}
  .btn{position:absolute;width:94px;height:45px;border-radius:4px;background:linear-gradient(var(--btn-top),var(--btn-bottom));
    color:#111;font-size:14px;display:flex;align-items:center;justify-content:center;border:1px solid #888}
  .card-tall .btn{left:84px;top:226px}
  .card-wide .btn{left:286px;top:83px}
  .site-footer{position:absolute;left:159px;top:950px;width:882px;height:168px;background:var(--footer-bg);border-radius:7px;font-size:11px;line-height:15px}
  .footer-text{position:absolute;left:39px;top:33px;width:620px}
  .footer-text p+p{margin-top:15px}
  .footer-links{position:absolute;left:39px;top:130px;color:var(--link-blue);font-weight:700;font-size:11px}
  .footer-links span.sep{color:#6a7a6a;margin:0 6px;font-weight:400}
  .follow{position:absolute;left:707px;top:33px;font-size:9px;letter-spacing:.3px;color:#ddd}
  .social{position:absolute;left:707px;top:52px;display:flex;gap:5px}
  .social span{width:20px;height:20px;border-radius:50%;background:#6a8cc2}
  .legal{position:absolute;left:707px;top:102px;list-style:none;font-size:11px;line-height:24px}
  .legal li::before{content:"";display:inline-block;border-left:4px solid var(--white);border-top:3px solid transparent;border-bottom:3px solid transparent;margin-right:5px}
</style>
</head>
<body>
<header class="site-header">
  <div class="brand">
    <div class="brand-mark"></div>
    <div>
      <div class="brand-name">Plove Tax Works</div>
      <div class="brand-tagline">Chartered Accountants &amp; Registered Tax Agent</div>
    </div>
  </div>
  <div class="account">
    <svg width="20" height="22" viewBox="0 0 20 22"><circle cx="10" cy="6" r="5" fill="#fff"/><path d="M0 22v-4c0-4 4-6 10-6s10 2 10 6v4z" fill="#fff"/></svg>
    My Account
  </div>
  <div class="phone">Call (02) 5550 1842</div>
  <nav class="main-nav">
    <a style="left:0">SERVICE</a>
    <a style="left:93px">TESTIMONIALS</a>
    <a style="left:226px">EVENTS</a>
    <a style="left:313px">PARTNER</a>
    <a style="left:413px">BLOG</a>
    <a style="left:492px">CONTACT US</a>
  </nav>
  <div class="search">Search
    <svg width="15" height="15" viewBox="0 0 15 15"><circle cx="6" cy="6" r="4.5" stroke="#888" stroke-width="1.6" fill="none"/><path d="M9.5 9.5l4 4" stroke="#888" stroke-width="2"/></svg>
  </div>
</header>

<section class="hero">
  <h1 class="hero-title">Vitae<br>Labores</h1>
  <div class="hero-art" role="img" aria-label="Illustration of three overlapping currency coins: dollar, yen and euro"></div>
</section>

<section class="features">
  <article class="card card-tall" style="left:159px">
    <h2>Ubique nobis</h2>
    <p>Congue aliquam epicuri sed ex. Vel iudico fabellas pertinacia ea, id ius graece tritani dolorem. Stet sapientem ne mei, te nec</p>
    <a class="btn">Read more</a>
  </article>
  <article class="card card-tall" style="left:469px">
    <h2>Ubique nobis</h2>
    <p>Congue aliquam epicuri sed ex. Vel iudico fabellas pertinacia ea, id ius graece tritani dolorem. Stet sapientem ne mei, te nec</p>
    <a class="btn">Read more</a>
  </article>
  <article class="card card-tall" style="left:778px">
    <h2>Ubique nobis</h2>
    <p>Congue aliquam epicuri sed ex. Vel iudico fabellas pertinacia ea, id ius graece tritani dolorem. Stet sapientem ne mei, te nec</p>
    <a class="btn">Read more</a>
  </article>
  <article class="card card-wide" style="left:159px">
    <h2>Ubique nobis</h2>
    <p>Congue aliquam epicuri sed ex. Vel iudico fabellas pertinacia ea, id ius</p>
    <a class="btn">Read more</a>
  </article>
  <article class="card card-wide" style="left:623px">
    <h2>Ubique nobis</h2>
    <p>Congue aliquam epicuri sed ex. Vel iudico fabellas pertinacia ea, id ius</p>
    <a class="btn">Read more</a>
  </article>
</section>

<footer class="site-footer">
  <div class="footer-text">
    <p>Sit libris legimus efficiantur id. His feugiat tractatos ne, corpora forensibus qui ut. No propriae albucius eam. Eius omnium cum in.</p>
    <p>Usu vide iudicabit ex. Libris voluptua vix in, falli nobis necessitatibus per ut. An sit vidit invidunt definiebas, eum quas tacimates assueverit ex. Ut magna velit iracundia mea, ei reque homero principes duo.</p>
  </div>
  <div class="footer-links">Libris<span class="sep">|</span>Legimus<span class="sep">|</span>Efficiantur<span class="sep">|</span>Feugiat<span class="sep">|</span>Tractatos<span class="sep">|</span>Corpora<span class="sep">|</span>Forensibus<span class="sep">|</span>Propriae</div>
  <div class="follow">FOLLOW US</div>
  <div class="social"><span></span><span></span><span></span><span></span><span></span></div>
  <ul class="legal">
    <li>Terms and Conditions</li>
    <li>Privacy Policy</li>
  </ul>
</footer>
</body>
</html>
```